This will turn into a huge project with mass exposure.

Tallow Crest creates soap, perfumes, rubs, lotion, etc for some of the most know brands in the market: Marisol Veil, Fern & Pebble Supply, PGR sports teams, etc.

They are going to be redesigning all logos, labels, websites and print.

They are starting with a business card and logo.

ALL designs must include a logo for Tallow Crest Holdings
Updates

Target Market(s)

Purchasers such as Marisl Veil

Industry/Entity Type

Business

Requirements
Must have
• a space for Qr code

two sided

Info:
Gavin Torlek, President
info@tallowcrest.example
555-014-2783
Nice to have
• Colors: gray background with blue and green tones. A globe that looks like an ancient map.

```html
<!DOCTYPE html>
<html lang="en">
<head>
<meta charset="utf-8">
<title>Tallow Crest – Business Card</title>
<link rel="stylesheet" href="https://fonts.googleapis.com/css2?family=Cinzel:wght@400;600;700&family=Crimson+Text:ital,wght@1,400;1,700&display=swap">
<style>
  :root {
    --page-bg: #f5fbf5;
    --label-ink: #111111;
    --front-light: #8d9094;
    --front-mid: #555a60;
    --front-dark: #30353d;
    --logo-green: #2cf02a;
    --logo-mark: #cdd88e;
    --back-green-dark: #2b8a2c;
    --back-green-light: #80f7b6;
    --name-ink: #163016;
    --body-ink: #0f1f12;
    --qr-fill: #f4fbf6;
    --qr-edge: #1d4a24;
    --card-shadow: 6px 9px 10px rgba(0, 0, 0, 0.6);
  }

  html, body {
    margin: 0;
    padding: 0;
    width: 1200px;
    height: 900px;
    overflow: hidden;
    background: var(--page-bg);
  }

  .sheet {
    position: relative;
    width: 1200px;
    height: 900px;
  }

  .side-label {
    position: absolute;
    margin: 0;
    font-family: "Cinzel", serif;
    font-weight: 400;
    font-size: 34px;
    color: var(--label-ink);
    letter-spacing: 1px;
  }
  .side-label--front { left: 788px; top: 70px; }
  .side-label--back  { left: 275px; top: 730px; }

  .card {
    position: absolute;
    overflow: hidden;
    box-shadow: var(--card-shadow);
  }

  /* Front */
  .card--front {
    left: 28px;
    top: 18px;
    width: 734px;
    height: 392px;
    background: radial-gradient(ellipse 420px 300px at 330px 215px,
      var(--front-light) 0%, var(--front-mid) 45%, var(--front-dark) 100%);
  }

  .front-map {
    position: absolute;
    left: 70px;
    top: 40px;
    width: 480px;
    height: 380px;
    border-radius: 50%;
    background: radial-gradient(ellipse at 50% 50%,
      rgba(28, 127, 192, 0.30) 0%, rgba(28, 127, 192, 0.18) 55%, rgba(28, 127, 192, 0) 75%);
  }

  .logo {
    position: absolute;
    left: 0;
    top: 100px;
    width: 734px;
    margin: 0;
    font-family: "Cinzel", serif;
    font-weight: 600;
    color: var(--logo-green);
    line-height: 1;
    display: flex;
    flex-direction: column;
    align-items: center;
  }
  .logo__line {
    display: flex;
    align-items: center;
    font-size: 78px;
    letter-spacing: 2px;
  }
  .logo__line + .logo__line { margin-top: 14px; }
  .logo__mark {
    display: block;
    width: 96px;
    height: 96px;
    margin-right: 14px;
    border-radius: 50%;
    background: var(--logo-mark);
  }

  /* Back */
  .card--back {
    left: 395px;
    top: 476px;
    width: 735px;
    height: 390px;
    background: linear-gradient(to bottom,
      var(--back-green-dark) 0%, var(--back-green-dark) 12%,
      var(--back-green-light) 55%,
      var(--back-green-dark) 88%, var(--back-green-dark) 100%);
  }

  .back-globe {
    position: absolute;
    left: 340px;
    top: -10px;
    width: 460px;
    height: 460px;
    border-radius: 50%;
    background: radial-gradient(circle at 45% 45%,
      rgba(185, 232, 207, 0.75) 0%, rgba(120, 200, 160, 0.55) 60%, rgba(79, 159, 120, 0.45) 100%);
  }

  .contact {
    position: absolute;
    left: 40px;
    top: 108px;
    width: 385px;
    text-align: center;
  }
  .contact__name {
    margin: 0;
    font-family: "Cinzel", serif;
    font-weight: 400;
    font-size: 44px;
    color: var(--name-ink);
    letter-spacing: 1px;
    text-shadow: 2px 3px 4px rgba(0, 0, 0, 0.5);
    white-space: nowrap;
  }
  .contact__title {
    margin: 8px 0 0;
    font-family: "Crimson Text", serif;
    font-style: italic;
    font-weight: 700;
    font-size: 24px;
    color: var(--name-ink);
    text-shadow: 1px 2px 3px rgba(0, 0, 0, 0.45);
  }
  .contact__details {
    margin: 50px 0 0;
    font-family: "Crimson Text", serif;
    font-style: italic;
    font-weight: 400;
    font-size: 20px;
    line-height: 29px;
    color: var(--body-ink);
    white-space: nowrap;
  }

  .qr-space {
    position: absolute;
    left: 24px;
    bottom: 22px;
    width: 78px;
    height: 78px;
    box-sizing: border-box;
    background: var(--qr-fill);
    border: 2px solid var(--qr-edge);
  }
</style>
</head>
<body>
  <main class="sheet">
    <p class="side-label side-label--front">FRONT</p>
    <p class="side-label side-label--back">BACK</p>

    <section class="card card--front">
      <div class="front-map" role="img" aria-label="Faint blue world map in the background"></div>
      <h1 class="logo" aria-label="Tallow Crest">
        <span class="logo__line">Tallow</span>
        <span class="logo__line"><span class="logo__mark"></span>Crest</span>
      </h1>
    </section>

    <section class="card card--back">
      <div class="back-globe" role="img" aria-label="Antique-map globe in soft green tones"></div>
      <div class="contact">
        <h2 class="contact__name">Gavin Torlek</h2>
        <p class="contact__title">president</p>
        <p class="contact__details">
          email: info@tallowcrest.example<br>
          phone: 555-014-2783
        </p>
      </div>
      <div class="qr-space" role="img" aria-label="Space reserved for QR code"></div>
    </section>
  </main>
</body>
</html>
```